Business card design needed

I need a business card design for a dog walking, dog minding and dog training business. Please refer to my website for the basic company colours and fonts I'm after. Planning on a double sided card, so all information doesn't need to be on the 'front' side.
Cheers

Industry/Entity Type

Dog Training

Contact Information for Business Card

Meadow Paws - happy hounds
Rua 0498307164
meadowpawsdemo.com.au
-walking
-holiday stays
-onsite care
-training and behavioural consultations

```html
<!DOCTYPE html>
<html lang="en">
<head>
<meta charset="utf-8">
<title>Meadow Paws – Business Card</title>
<link rel="stylesheet" href="https://fonts.googleapis.com/css2?family=Questrial&family=Mulish:wght@600;700;800&display=swap">
<style>
  :root {
    --brand-orange: #e04a26;
    --brand-orange-light: #ec5530;
    --ink-grey: #4a4a4a;
    --paper: #f3f3f3;
    --paper-shade: #dcdcdc;
    --rule: #7a7a7a;
    --backdrop: #e9e7e4;
    --white: #ffffff;
    --photo-tone: #c89a6a;
  }
  html, body {
    margin: 0;
    padding: 0;
    width: 1200px;
    height: 1181px;
    overflow: hidden;
    background: var(--backdrop);
  }
  .canvas {
    position: relative;
    width: 1200px;
    height: 1181px;
  }
  .card {
    position: absolute;
    left: 237px;
    width: 726px;
    height: 419px;
    overflow: hidden;
    box-shadow: 0 4px 14px rgba(0,0,0,0.25);
  }

  /* Front */
  .card-front {
    top: 126px;
    background: radial-gradient(ellipse at 50% 40%, var(--white) 0%, var(--paper) 45%, var(--paper-shade) 100%);
  }
  .band {
    position: absolute;
    left: 0;
    width: 100%;
    height: 31px;
    background: var(--brand-orange);
  }
  .band-top { top: 0; }
  .band-bottom { bottom: 0; }
  .wordmark {
    position: absolute;
    top: 176px;
    left: 0;
    width: 100%;
    text-align: center;
    font-family: "Questrial", sans-serif;
    font-size: 50px;
    letter-spacing: 1px;
    line-height: 1;
    color: var(--ink-grey);
  }
  .services {
    position: absolute;
    top: 243px;
    left: 218px;
    width: 290px;
    border-top: 1px solid var(--rule);
    border-bottom: 1px solid var(--rule);
    padding: 4px 0 5px;
    text-align: center;
    font-family: "Mulish", sans-serif;
    font-weight: 700;
    font-size: 10.5px;
    line-height: 13px;
    color: #333;
  }
  .photo-slot {
    position: absolute;
    left: 296px;
    top: 312px;
    width: 142px;
    height: 82px;
  }

  /* Back */
  .card-back {
    top: 628px;
    background: radial-gradient(ellipse at 50% 45%, var(--brand-orange-light) 0%, var(--brand-orange) 70%, #d6421f 100%);
    color: var(--white);
  }
  .side-label {
    position: absolute;
    top: 50%;
    white-space: nowrap;
    line-height: 1;
    transform-origin: center;
  }
  .side-brand {
    left: 46px;
    font-family: "Questrial", sans-serif;
    font-size: 42px;
    letter-spacing: 1px;
    transform: translate(-50%, -50%) rotate(-90deg);
  }
  .side-tagline {
    left: 694px;
    font-family: "Mulish", sans-serif;
    font-weight: 700;
    font-size: 23px;
    letter-spacing: 1.5px;
    transform: translate(-50%, -50%) rotate(-90deg);
  }
  .contact {
    position: absolute;
    top: 152px;
    left: 0;
    width: 100%;
    text-align: center;
    font-family: "Mulish", sans-serif;
  }
  .contact-name {
    font-weight: 800;
    font-size: 58px;
    line-height: 1;
    margin: 0 0 14px;
  }
  .contact-line {
    font-weight: 700;
    font-size: 16px;
    line-height: 22px;
    margin: 0;
  }
</style>
</head>
<body>
<main class="canvas">

  <section class="card card-front" aria-label="Card front">
    <div class="band band-top"></div>
    <div class="wordmark">MEADOW PAWS</div>
    <div class="services">
      Walking - Holiday stays - Onsite care<br>
      Training and Behavioural consultations
    </div>
    <svg class="photo-slot" viewBox="0 0 142 82" role="img" aria-label="Photo of a puppy peeking over the bottom band">
      <defs>
        <radialGradient id="photoTone" cx="50%" cy="45%" r="60%">
          <stop offset="0%" stop-color="#f1ece6"/>
          <stop offset="100%" stop-color="var(--photo-tone)"/>
        </radialGradient>
      </defs>
      <rect x="0" y="0" width="142" height="82" rx="10" fill="url(#photoTone)"/>
    </svg>
    <div class="band band-bottom"></div>
  </section>

  <section class="card card-back" aria-label="Card back">
    <div class="side-label side-brand">MEADOW PAWS</div>
    <div class="contact">
      <p class="contact-name">RUA</p>
      <p class="contact-line">0498307164</p>
      <p class="contact-line">meadowpawsdemo.com.au</p>
    </div>
    <div class="side-label side-tagline">HAPPY HOUNDS</div>
  </section>

</main>
</body>
</html>
```